Harborline Estates Business Card for Apartment Buildings

Create business cards for resident managers who run apartment buildings. The audience is the public who are searching for apartment rentals, and current residents who live at the apartment building. Key design element will be incorporating the company logo, however, the logo cannot dominate. The building name and manager name are more important than the logo. Current business card design leaves little room for copy, so we may need to reduce the size on the current card to allow for more space for copy.

Target Market(s)

Adults 18-65 years of age, who are looking for an apartment rental, plus current residents who live at our apartment buildings.

Industry/Entity Type

Property Management

Contact Information for Business Card

A major design element will be use of the company logo. Important property and manager contact information must be part of the design. The size of the logo will need to be reduced to make room for building and manager contact copy.

Font styles to use
Sans Serif

Colors
3176b5
000000
959595
ffffff

Requirements
Must have
• 1) Incorporate the company logo.
• 2) Use the company colors (dark blue, black/grey, over white).
• 3) FEATURE THE BUILDING NAME
• 4) FEATURE THE MANAGER NAME
• 5) The company name is less important than BUILDING and MANAGER
• 6) Manager contact information
• **SEE ATTACHED CREATIVE BRIEF**
Nice to have
• 1) Back of card logo watermark
• 2) Ability to write notes on back of carfd
Should not have
• Avoid letting the company logo dominate the card, the building name and manager are more important than the company logo.

```html
<!DOCTYPE html>
<html lang="en">
<head>
<meta charset="utf-8">
<title>Harborline Estates — Business Card</title>
<link rel="stylesheet" href="https://fonts.googleapis.com/css2?family=Oswald:wght@600&family=Roboto:wght@400;700&display=swap">
<style>
  :root {
    --brand-blue: #3176b5;
    --card-grey: #46464a;
    --card-grey-dark: #3e3e42;
    --mid-grey: #959595;
    --ink: #000000;
    --paper: #ffffff;
    --backdrop: #e9e9eb;
  }
  * { margin: 0; padding: 0; box-sizing: border-box; }
  html, body { width: 1200px; height: 930px; overflow: hidden; }
  body {
    background: var(--backdrop);
    font-family: "Roboto", Arial, sans-serif;
    position: relative;
  }
  .card {
    position: absolute;
    width: 520px;
    height: 310px;
    border-radius: 14px;
    overflow: hidden;
    box-shadow: 0 6px 18px rgba(0,0,0,0.18);
  }

  /* Back of card */
  .card-back {
    left: 70px;
    top: 120px;
    background: var(--card-grey);
  }
  .card-back .texture {
    position: absolute;
    inset: 0;
    background: radial-gradient(circle at 50% 45%, #4d4d51 0%, var(--card-grey-dark) 100%);
  }
  .back-brand {
    position: absolute;
    left: 0; right: 0;
    top: 116px;
    display: flex;
    align-items: center;
    justify-content: center;
    gap: 12px;
    color: var(--paper);
    font-weight: 700;
  }
  .brand-dot {
    width: 30px; height: 30px;
    border-radius: 50%;
    background: currentColor;
    flex: none;
  }
  .brand-name { line-height: 1; white-space: nowrap; }
  .back-brand .brand-name { font-size: 28px; letter-spacing: 1px; }
  .back-url {
    position: absolute;
    left: 0; right: 0;
    bottom: 54px;
    text-align: center;
    color: var(--paper);
    font-size: 15px;
    letter-spacing: 0.5px;
  }

  /* Front of card */
  .card-front {
    left: 610px;
    top: 480px;
    background: var(--card-grey);
  }
  .card-front svg.sweep {
    position: absolute;
    inset: 0;
  }
  .front-brand {
    position: absolute;
    right: 30px;
    top: 40px;
    display: flex;
    align-items: center;
    gap: 8px;
    color: var(--brand-blue);
    font-weight: 700;
  }
  .front-brand .brand-dot { width: 20px; height: 20px; }
  .front-brand .brand-name { font-size: 20px; letter-spacing: 0.5px; }
  .property {
    position: absolute;
    right: 30px;
    top: 84px;
    text-align: right;
  }
  .property-name {
    color: var(--brand-blue);
    font-size: 16px;
    font-weight: 400;
  }
  .property-address {
    color: #555;
    font-size: 13px;
    margin-top: 3px;
  }
  .manager {
    position: absolute;
    left: 30px;
    bottom: 20px;
    color: var(--paper);
  }
  .manager-name {
    font-family: "Oswald", "Arial Narrow", sans-serif;
    font-weight: 600;
    font-size: 22px;
    letter-spacing: 0.5px;
    text-transform: uppercase;
    line-height: 1.1;
    white-space: nowrap;
  }
  .manager-title { font-size: 13px; margin-bottom: 8px; }
  .contact-list { list-style: none; font-size: 13px; }
  .contact-list li {
    display: flex;
    align-items: center;
    gap: 9px;
    line-height: 18px;
  }
  .contact-list svg { width: 11px; height: 11px; flex: none; fill: var(--paper); }
</style>
</head>
<body>

  <section class="card card-back" aria-label="Back of business card">
    <div class="texture" role="img" aria-label="Faint repeating brand watermark texture on dark grey"></div>
    <div class="back-brand">
      <span class="brand-dot"></span>
      <span class="brand-name">HARBORLINE ESTATES LLC</span>
    </div>
    <p class="back-url">www.harborlineest.com</p>
  </section>

  <section class="card card-front" aria-label="Front of business card">
    <svg class="sweep" viewBox="0 0 520 310" preserveAspectRatio="none" aria-hidden="true">
      <path d="M150,0 C175,150 290,240 520,222 L520,0 Z" fill="var(--paper)"/>
      <path d="M144,0 C169,152 286,246 520,227" fill="none" stroke="var(--brand-blue)" stroke-width="4"/>
    </svg>

    <div class="front-brand">
      <span class="brand-dot"></span>
      <span class="brand-name">HARBORLINE ESTATES LLC</span>
    </div>

    <div class="property">
      <p class="property-name">Cedar Court Apartments</p>
      <p class="property-address">1482 Linden Avenue Bayview, CA 90000</p>
    </div>

    <div class="manager">
      <h1 class="manager-name">Marisol Delgado</h1>
      <p class="manager-title">Resident Manager</p>
      <ul class="contact-list">
        <li><svg viewBox="0 0 12 12"><path d="M2 1h3l1 3-1.5 1a7 7 0 0 0 2.5 2.5L8 6l3 1v3c-5 0-9-4-9-9z"/></svg>555-014-2231</li>
        <li><svg viewBox="0 0 12 12"><path d="M3 0h6v12H3zM4 1v8h4V1z"/></svg>555-017-4408</li>
        <li><svg viewBox="0 0 12 12"><path d="M3 0h6v4H3zM1 5h10v5H1zM3 9h6v3H3z"/></svg>555-019-3350</li>
        <li><svg viewBox="0 0 12 12"><path d="M0 2h12v8H0zM1 3l5 4 5-4v-.2H1z"/></svg>marisol@harborlineest.com</li>
        <li><svg viewBox="0 0 12 12"><circle cx="6" cy="6" r="5.5"/></svg>www.harborlineest.com</li>
      </ul>
    </div>
  </section>

</body>
</html>
```